Front page on www.brightvalemerch.com modern service ads - each ad for each featured service

We need to have initial 5 banners to be created for our soon to be launched new site,. These are 5 rotating banners that will showcase our companies key features. We are looking for a modern stylish yet simple look to highlight these features. Something thats very inviting and modern to fit the look of the new website.

5 banners need to be, information can be found on www.brightvalemerch.com about these. Please ask if any questions

Why us?
Art Services
Order Process
Current promotions
Clearance products

please also note. the design will be going onto this website. http://new.brightvalemerch.com/ Please base actual designs , color schemes etc.. for the new site.

Target Market(s)

Small businesses that purchase marketing promotional goods, to promote their business

Industry/Entity Type

Promotional Product

Font styles to use
Sans Serif

Requirements
Must have
• Size of the banner is 965 x 400 px
Nice to have
• Modern elements,, very clean and minimal look
Should not have
• no cheap generic clip art

```html
<!DOCTYPE html>
<html lang="en">
<head>
<meta charset="utf-8">
<title>Order Process – Brightvale Merch</title>
<link href="https://fonts.googleapis.com/css2?family=Montserrat:ital,wght@1,600;1,800;1,900&display=swap" rel="stylesheet">
<style>
  :root {
    --ink: #2d4250;
    --bg-light: #f5f7f8;
    --bg-mid: #e9edf0;
    --sky: #4cc4f5;
    --mint: #2ee89a;
    --icon: #39e0a0;
    --photo-top: #c9c9c9;
    --photo-bottom: #5aa0c4;
  }
  html, body { margin: 0; padding: 0; overflow: hidden; }
  .banner { display: block; width: 1200px; height: 497px; }
  .title { font-family: "Montserrat", sans-serif; font-style: italic; font-weight: 900; fill: var(--ink); letter-spacing: 1px; }
  .step-label { font-family: "Montserrat", sans-serif; font-style: italic; font-weight: 600; font-size: 11.5px; fill: var(--ink); text-anchor: middle; }
  .step-num { font-family: "Montserrat", sans-serif; font-style: italic; font-weight: 800; font-size: 13px; }
  .num-sky { fill: var(--sky); }
  .num-mint { fill: var(--mint); }
  .step-disc { fill: var(--ink); }
  .icon { fill: none; stroke: var(--icon); stroke-width: 1.6; stroke-linecap: round; stroke-linejoin: round; }
  .arrow { fill: var(--ink); }
</style>
</head>
<body>
<svg class="banner" viewBox="0 0 965 400" preserveAspectRatio="none" xmlns="http://www.w3.org/2000/svg">
  <defs>
    <linearGradient id="bgFade" x1="0" y1="0" x2="1" y2="1">
      <stop offset="0" stop-color="var(--bg-light)"/>
      <stop offset="1" stop-color="var(--bg-mid)"/>
    </linearGradient>
    <linearGradient id="photoFill" x1="0" y1="0" x2="0" y2="1">
      <stop offset="0" stop-color="var(--photo-top)"/>
      <stop offset="1" stop-color="var(--photo-bottom)"/>
    </linearGradient>
    <radialGradient id="dotHaze" cx="0.5" cy="0.5" r="0.5">
      <stop offset="0" stop-color="var(--mint)" stop-opacity="0.12"/>
      <stop offset="1" stop-color="var(--mint)" stop-opacity="0"/>
    </radialGradient>
    <g id="arrowMark" class="arrow">
      <rect x="0" y="-1.6" width="3" height="3.2"/>
      <rect x="5" y="-1.6" width="3" height="3.2"/>
      <path d="M10 -7 L22 0 L10 7 Z"/>
    </g>
  </defs>

  <!-- background -->
  <rect class="canvas-bg" width="965" height="400" fill="url(#bgFade)"/>
  <rect class="dot-field" x="280" y="0" width="340" height="400" fill="url(#dotHaze)" role="img" aria-label="Soft field of small green dots"/>
  <circle class="accent-mint" cx="905" cy="22" r="72" fill="var(--mint)"/>

  <!-- hero ring and photo -->
  <circle class="accent-sky" cx="148" cy="140" r="202" fill="var(--sky)"/>
  <circle class="hero-photo" cx="128" cy="142" r="150" fill="url(#photoFill)" role="img" aria-label="Smiling delivery worker in a blue cap and polo holding out a branded cardboard box"/>

  <!-- heading -->
  <text class="title" x="400" y="86" font-size="60">ORDER PROCESS</text>

  <!-- row 1 -->
  <g class="step">
    <circle class="step-disc" cx="470" cy="170" r="37"/>
    <g class="icon"><rect x="454" y="156" width="30" height="24" rx="2"/><line x1="454" y1="162" x2="484" y2="162"/><path d="M470 168 v12 l3 -3 l3 5"/></g>
    <text class="step-num num-sky" x="498" y="196">1</text>
    <text class="step-label" x="470" y="215">Place Order</text>
  </g>
  <use href="#arrowMark" x="519" y="164"/>
  <g class="step">
    <circle class="step-disc" cx="592" cy="170" r="37"/>
    <g class="icon"><rect x="578" y="155" width="28" height="30" rx="2"/><line x1="592" y1="155" x2="592" y2="185"/><circle cx="585" cy="164" r="3"/><path d="M596 178 l4 -6 l4 6"/></g>
    <text class="step-num num-mint" x="620" y="196">2</text>
    <text class="step-label" x="592" y="215">Submit Artwork</text>
  </g>
  <use href="#arrowMark" x="641" y="164"/>
  <g class="step">
    <circle class="step-disc" cx="717" cy="170" r="37"/>
    <g class="icon"><circle cx="719" cy="170" r="14"/><path d="M719 161 v9 l6 4"/><line x1="697" y1="165" x2="703" y2="165"/><line x1="695" y1="171" x2="702" y2="171"/><line x1="697" y1="177" x2="703" y2="177"/></g>
    <text class="step-num num-sky" x="745" y="196">3</text>
    <text class="step-label" x="717" y="215">Proof in 24-48 hours</text>
  </g>
  <use href="#arrowMark" x="766" y="164"/>
  <g class="step">
    <circle class="step-disc" cx="840" cy="170" r="37"/>
    <g class="icon"><circle cx="840" cy="170" r="15"/><circle cx="840" cy="170" r="10"/><path d="M835 170 l4 4 l7 -8"/></g>
    <text class="step-num num-mint" x="868" y="196">4</text>
    <text class="step-label" x="840" y="215">Approve Proof</text>
  </g>

  <!-- row 2 -->
  <use href="#arrowMark" x="398" y="273"/>
  <g class="step">
    <circle class="step-disc" cx="470" cy="280" r="37"/>
    <g class="icon"><circle cx="470" cy="280" r="7"/><path d="M470 264 v4 M470 292 v4 M454 280 h4 M482 280 h4 M459 269 l3 3 M478 288 l3 3 M459 291 l3 -3 M478 272 l3 -3"/></g>
    <text class="step-num num-mint" x="498" y="306">5</text>
    <text class="step-label" x="470" y="325">Production Begins</text>
  </g>
  <use href="#arrowMark" x="519" y="273"/>
  <g class="step">
    <circle class="step-disc" cx="592" cy="280" r="37"/>
    <g class="icon"><rect x="577" y="266" width="28" height="26" rx="2"/><line x1="577" y1="273" x2="605" y2="273"/><path d="M583 262 v6 M599 262 v6"/><path d="M595 286 l3 3 l6 -6"/></g>
    <text class="step-num num-sky" x="620" y="306">6</text>
    <text class="step-label" x="592" y="325">Ship Date Set</text>
  </g>
  <use href="#arrowMark" x="641" y="273"/>
  <g class="step">
    <circle class="step-disc" cx="717" cy="280" r="37"/>
    <g class="icon"><rect x="702" y="265" width="12" height="10" rx="1"/><path d="M708 275 v6 h18 v6 h-20"/><path d="M728 283 c0 -7 -9 -7 -9 0 c0 4 4.5 8 4.5 8 s4.5 -4 4.5 -8"/></g>
    <text class="step-num num-sky" x="745" y="306">7</text>
    <text class="step-label" x="717" y="325">Track Shipping</text>
  </g>
  <use href="#arrowMark" x="766" y="273"/>
  <g class="step">
    <circle class="step-disc" cx="840" cy="280" r="37"/>
    <g class="icon"><path d="M828 263 h18 l6 6 v26 h-24 Z"/><line x1="833" y1="276" x2="845" y2="276"/><line x1="833" y1="281" x2="841" y2="281"/><circle cx="848" cy="289" r="6"/><path d="M845.5 289 l2 2 l3 -3.5"/></g>
    <text class="step-num num-sky" x="868" y="306">8</text>
    <text class="step-label" x="840" y="325">Final Invoice</text>
  </g>
</svg>
</body>
</html>
```